Business card for Chicago based Private Equity Company

We need a business card for our PE company called Crestline Partners. We want a simple and clean, yet creative card design. The back side should reflect our logo. Also would like to see embossed ideas. Should reflect strength and growth. Our logo is attached. Also need editable file. Details are as follows for Business Card:

Dale Moravec Co-Founder 2750 Larkin Avenue Suite 410 Oak Brook, IL 60587 http://www.crestlinepartnersllc.example (D) 630.555.0142 (C) 312.555.0178 (E) dm@crestlinepartnersllc.example

```html
<!DOCTYPE html>
<html lang="en">
<head>
<meta charset="utf-8">
<title>Crestline Partners – Business Card</title>
<link rel="stylesheet" href="https://fonts.googleapis.com/css2?family=PT+Sans+Narrow:wght@400;700&display=swap">
<style>
  :root {
    --backdrop: #8d8d8d;
    --card: #3b3b3b;
    --ink: #121212;
    --edge: #2f2f2f;
  }
  * { box-sizing: border-box; margin: 0; padding: 0; }
  html, body {
    width: 1200px;
    height: 900px;
    overflow: hidden;
    background: var(--backdrop);
    font-family: "PT Sans Narrow", "Arial Narrow", sans-serif;
  }
  .canvas {
    position: relative;
    width: 1200px;
    height: 900px;
  }
  .card {
    position: absolute;
    width: 660px;
    height: 377px;
    background: var(--card);
    border: 1px solid var(--edge);
    color: var(--ink);
  }
  .card--back { left: 400px; top: 56px; }
  .card--front { left: 140px; top: 467px; }

  /* Back side */
  .wordmark {
    position: absolute;
    left: 0; right: 0; top: 0; bottom: 0;
    display: flex;
    align-items: center;
    justify-content: center;
    font-weight: 700;
    font-size: 58px;
    letter-spacing: 0.12em;
    text-transform: uppercase;
  }

  /* Front side */
  .person {
    position: absolute;
    left: 58px;
    top: 48px;
    text-transform: uppercase;
    font-weight: 700;
  }
  .person__name { font-size: 30px; line-height: 1; }
  .person__title { font-size: 17px; margin-top: 4px; }

  .brand {
    position: absolute;
    left: 58px;
    top: 170px;
    display: flex;
    align-items: center;
    gap: 14px;
  }
  .brand__dot { width: 90px; height: 90px; flex: none; }
  .brand__name {
    font-weight: 700;
    font-size: 20px;
    text-transform: uppercase;
    letter-spacing: 0.04em;
  }

  .contact {
    position: absolute;
    right: 36px;
    bottom: 34px;
    text-align: right;
    text-transform: uppercase;
    font-weight: 700;
    font-size: 16px;
    line-height: 1.3;
    font-style: normal;
  }
</style>
</head>
<body>
  <main class="canvas">
    <section class="card card--back" aria-label="Card back">
      <div class="wordmark">Crestline Partners</div>
    </section>

    <section class="card card--front" aria-label="Card front">
      <div class="person">
        <p class="person__name">Dale Moravec</p>
        <p class="person__title">Co-Founder</p>
      </div>

      <div class="brand">
        <svg class="brand__dot" viewBox="0 0 90 90" aria-hidden="true">
          <circle cx="45" cy="45" r="40" fill="none" stroke="#121212" stroke-width="7"/>
        </svg>
        <span class="brand__name">Crestline Partners</span>
      </div>

      <address class="contact">
        <p>Tel 630.555.0142 / 312.555.0178</p>
        <p>crestlinepartnersllc.example</p>
        <p>dm@crestlinepartnersllc.example</p>
        <p>2750 Larkin Avenue Suite 410 Oak Brook, IL 60587</p>
      </address>
    </section>
  </main>
</body>
</html>
```